New to PixelMarket? This contest is just for you!

Are you new to PixelMarket and looking to enter your first contest? Look no further!

Requirements:
* We want you to create a beautiful and eye-catching graphic design which contains the words "Find me on PixelMarket"
* Your design should be unique and showcase your personality as a designer!
* You must be new to PixelMarket (registered in June 2015) to be eligible for prizes
* You must upload your entry before 12:00am 1 July Australian Eastern Standard Time

Conditions of Entry:
* This contest is only open to designers who opened their account this month (June 2015)
* You should only submit 1 design to this contest
* Your design must adhere to our quality standards to be eligible to receive a prize

Prizes:
* First prize for the best design is $500
* Second prize is $250
* Third prize is $100
* Up to 30 x $5 participation payments ($100) available to be awarded to high-quality designs

```html
<!DOCTYPE html>
<html lang="en">
<head>
<meta charset="utf-8">
<title>Find me on PixelMarket</title>
<link rel="stylesheet" href="https://fonts.googleapis.com/css2?family=Pirata+One&family=Bodoni+Moda:wght@400&display=swap">
<style>
  :root {
    --bg: #ffffff;
    --door-tone: #c9a88a;
    --key-tone: #d9aa2a;
    --ink: #000000;
    --brand: #1f4a66;
  }
  html, body {
    margin: 0;
    padding: 0;
    overflow: hidden;
    background: var(--bg);
  }
  .canvas {
    position: relative;
    width: 1200px;
    height: 411px;
    background: var(--bg);
    overflow: hidden;
  }
  .headline {
    position: absolute;
    left: 0;
    top: 0;
  }
  .door-art {
    fill: var(--door-tone);
  }
  .key-art {
    fill: var(--key-tone);
  }
  .door-letter {
    font-family: "Pirata One", cursive;
    font-size: 200px;
    fill: var(--ink);
  }
  .tagline {
    position: absolute;
    left: 618px;
    top: 318px;
    margin: 0;
    display: flex;
    align-items: center;
    gap: 22px;
    font-family: "Bodoni Moda", serif;
    font-weight: 400;
    line-height: 1;
  }
  .tagline-on {
    font-size: 46px;
    color: var(--ink);
    letter-spacing: 1px;
  }
  .brand {
    display: flex;
    align-items: center;
    gap: 12px;
  }
  .brand-dot {
    width: 40px;
    height: 40px;
    border-radius: 50%;
    background: var(--brand);
  }
  .brand-name {
    font-size: 54px;
    color: var(--brand);
  }
</style>
</head>
<body>
<main class="canvas">
  <svg class="headline" width="1200" height="411" viewBox="0 0 1200 411" aria-label="Find me">
    <g class="door">
      <rect class="door-art" role="img" aria-label="Arched door illustration" x="0" y="30" width="145" height="255"/>
      <text class="door-letter" x="72" y="240" text-anchor="middle">F</text>
    </g>
    <g class="door">
      <rect class="door-art" role="img" aria-label="Arched door illustration" x="165" y="30" width="145" height="255"/>
      <text class="door-letter" x="237" y="240" text-anchor="middle">I</text>
    </g>
    <g class="door">
      <rect class="door-art" role="img" aria-label="Arched door illustration" x="330" y="30" width="145" height="255"/>
      <text class="door-letter" x="402" y="240" text-anchor="middle">N</text>
    </g>
    <g class="door">
      <rect class="door-art" role="img" aria-label="Arched door illustration" x="493" y="30" width="145" height="255"/>
      <text class="door-letter" x="565" y="240" text-anchor="middle">D</text>
    </g>

    <rect class="key-art" role="img" aria-label="Golden key illustration" x="685" y="30" width="80" height="255"/>

    <g class="door">
      <rect class="door-art" role="img" aria-label="Arched door illustration" x="820" y="30" width="145" height="255"/>
      <text class="door-letter" x="892" y="240" text-anchor="middle">M</text>
    </g>
    <g class="door">
      <rect class="door-art" role="img" aria-label="Arched door illustration" x="985" y="30" width="145" height="255"/>
      <text class="door-letter" x="1057" y="240" text-anchor="middle">E</text>
    </g>
  </svg>

  <p class="tagline">
    <span class="tagline-on">ON</span>
    <span class="brand">
      <span class="brand-dot"></span>
      <span class="brand-name">PixelMarket</span>
    </span>
  </p>
</main>
</body>
</html>
```